Vegan Jerky company needs a label for it's pouch, and a new logo

Dear Designers - this used to be a guaranteed project, however, due to the low quality of designs I have received, I have removed the guaranteed status. However, we need this product made and we will pay for a great, high quality design that meets the requirements of our brief.

We need sticker labels that will go onto the front and back of our vegan jerky package. Our package is a zip-sealable pouch, and we will either go with black, white or brown for the color of the pouch.

We need the concept, artwork, theme and logo designed. Pls choose the colors.

There will be four flavors. These can be finished as part of another project. The flavors are: Smoked Maple, Cracked Pepper, Teriyaki Sriracha, Original.

We are Lonny and Marva's Vegan Jerky.

Our food is vegan, non GMO, straight from the farm, organic, healthy, pure, clean, made in small batches and earth friendly. We use no chemicals or artificial flavors and our product is 100% natural.

Our kitchen is yours.
Updates

Low designer entries

Target Market(s)

Vegetarians, vegans, health conscious, ecological, intelligent, caring.

Industry/Entity Type

Food Production

Logo Text

"Lonny and Marva" and "Our Kitchen is Yours"

Colors

Designer to choose colors to be used in the design.

Requirements
Must have
• earth friendly design, classy, hipster, vegan design, shabby chic,
Nice to have
• i have no ideas really...
• We prefer black and while, with a little splash of color. The last file is an idea I had but please use your own vision.

```html
<!DOCTYPE html>
<html lang="en">
<head>
<meta charset="utf-8">
<title>Lonny and Marva's Vegan Jerky – Pouch Labels</title>
<link rel="stylesheet" href="https://fonts.googleapis.com/css2?family=Cormorant+Garamond:ital,wght@0,500;0,600;1,400;1,500&family=Arimo:wght@400;700&display=swap">
<style>
  :root {
    --page: #ffffff;
    --pouch: #161616;
    --pouch-edge: #2a2a2a;
    --zip: #2f2f2f;
    --ink-light: #e9e6e0;
    --ink-muted: #b9b6b0;
    --rule: #9c9a96;
    --sage: #6f8a4c;
    --maple: #d8a23a;
    --maple-ink: #2a1c08;
    --art-a: #3a3a3a;
    --art-b: #262626;
  }
  * { box-sizing: border-box; margin: 0; padding: 0; }
  html, body { width: 1200px; height: 960px; overflow: hidden; background: var(--page); }
  .canvas { position: relative; width: 1200px; height: 960px; }

  .pouch {
    position: absolute;
    overflow: hidden;
    background: linear-gradient(180deg, #1d1d1d 0%, var(--pouch) 40%, #121212 100%);
    border: 1px solid var(--pouch-edge);
    border-radius: 4px;
    color: var(--ink-light);
    font-family: "Cormorant Garamond", serif;
  }
  .pouch-zip { position: absolute; left: 0; right: 0; height: 1px; background: var(--zip); }

  /* Front label */
  .pouch-front { left: 100px; top: 54px; width: 516px; height: 852px; }
  .tagline {
    position: absolute; left: 98px; top: 186px; width: 330px;
    text-align: center;
    font-size: 14px; letter-spacing: 3px; text-transform: uppercase;
  }
  .brand-name {
    position: absolute; left: 98px; top: 220px; width: 340px;
    font-weight: 500; font-size: 56px; line-height: 1; letter-spacing: 1px;
    text-transform: uppercase; white-space: nowrap;
  }
  .established {
    position: absolute; left: 376px; top: 286px; width: 60px; text-align: center;
    font-size: 20px; line-height: 1.05; text-transform: uppercase;
  }
  .brand-rule { position: absolute; left: 98px; width: 330px; height: 1px; background: var(--rule); }
  .brand-descriptor {
    position: absolute; left: 98px; top: 350px; width: 330px; text-align: center;
    font-size: 31px; font-weight: 600; letter-spacing: 5px; line-height: 1;
    text-transform: uppercase; color: var(--sage);
  }
  .front-art { position: absolute; left: 158px; top: 468px; width: 200px; height: 212px; }
  .flavour-band {
    position: absolute; left: 93px; top: 700px; width: 330px; height: 42px;
    background: var(--maple); color: var(--maple-ink);
    display: flex; align-items: center; justify-content: center;
    font-size: 24px; font-weight: 500; letter-spacing: 1px; text-transform: uppercase;
    outline: 1px solid var(--maple); outline-offset: 3px;
  }
  .net-weight {
    position: absolute; left: 0; right: 0; top: 764px; text-align: center;
    font-size: 19px; line-height: 1.45; color: var(--ink-muted);
  }

  /* Back label */
  .pouch-back { left: 658px; top: 110px; width: 458px; height: 760px; }
  .back-frame {
    position: absolute; left: 24px; top: 161px; width: 410px; height: 515px;
    border: 1px solid var(--rule);
  }
  .back-art-left { position: absolute; left: 34px; top: 274px; width: 116px; height: 190px; }
  .back-art-right { position: absolute; left: 318px; top: 232px; width: 100px; height: 220px; }
  .story-intro {
    position: absolute; left: 24px; width: 410px; top: 176px; text-align: center; font-size: 16px;
  }
  .story-name {
    position: absolute; left: 24px; width: 410px; top: 198px; text-align: center;
    font-style: italic; font-size: 18px;
  }
  .story-body {
    position: absolute; left: 156px; top: 232px; width: 156px; text-align: center;
    font-style: italic; font-size: 13.5px; line-height: 1.3;
  }
  .story-sign {
    position: absolute; left: 156px; top: 440px; width: 200px; text-align: center;
    font-style: italic; font-size: 14.5px;
  }

  .nutrition {
    position: absolute; left: 36px; top: 492px; width: 190px;
    border: 1px solid var(--ink-light); padding: 4px 5px;
    font-family: "Arimo", sans-serif; font-size: 7px; line-height: 1.25;
  }
  .nutrition h3 { font-size: 8px; font-weight: 700; letter-spacing: 0.3px; }
  .nutrition table { width: 100%; border-collapse: collapse; margin-top: 4px; }
  .nutrition th { font-weight: 400; font-style: italic; font-size: 5px; text-align: left; border-bottom: 1px solid var(--rule); padding-bottom: 2px; }
  .nutrition td { padding: 0.5px 0; white-space: nowrap; }
  .nutrition td:first-child { font-weight: 700; }
  .nutrition .col-split { border-left: 1px solid var(--rule); padding-left: 3px; }
  .nutrition-note {
    position: absolute; left: 36px; top: 644px; width: 190px;
    font-family: "Arimo", sans-serif; font-size: 5.5px; line-height: 1.4; color: var(--ink-muted);
  }

  .product-info {
    position: absolute; left: 240px; top: 492px; width: 186px;
    font-family: "Arimo", sans-serif; font-size: 6px; line-height: 1.45; color: var(--ink-muted);
  }
  .product-info p { margin-bottom: 8px; }
  .product-info strong { color: var(--ink-light); }
  .claims { display: flex; gap: 22px; margin: 2px 0 12px 10px; text-align: center; color: var(--ink-light); }
</style>
</head>
<body>
<main class="canvas">

  <section class="pouch pouch-front" aria-label="Front label">
    <div class="pouch-zip" style="top:40px"></div>
    <div class="pouch-zip" style="top:62px"></div>

    <p class="tagline">Our Kitchen is Yours</p>
    <h1 class="brand-name">Lonny and<br>Marva's</h1>
    <p class="established">Est.<br>2018</p>
    <div class="brand-rule" style="top:340px"></div>
    <p class="brand-descriptor">Vegan Jerky</p>
    <div class="brand-rule" style="top:390px"></div>

    <svg class="front-art" role="img" aria-label="Sketch illustration of two farmers holding a basket of harvest" viewBox="0 0 200 212">
      <defs>
        <linearGradient id="frontArtTone" x1="0" y1="0" x2="0" y2="1">
          <stop offset="0" stop-color="#3a3a3a"/>
          <stop offset="1" stop-color="#262626"/>
        </linearGradient>
      </defs>
      <rect width="200" height="212" rx="4" fill="url(#frontArtTone)"/>
    </svg>

    <div class="flavour-band">Smoked Maple</div>
    <p class="net-weight">3oz/<br>80.05gr</p>
  </section>

  <section class="pouch pouch-back" aria-label="Back label">
    <div class="pouch-zip" style="top:34px"></div>
    <div class="pouch-zip" style="top:54px"></div>

    <div class="back-frame"></div>

    <svg class="back-art-left" role="img" aria-label="Sketch of a farmer carrying a basket" viewBox="0 0 116 190">
      <rect width="116" height="190" rx="4" fill="#333333"/>
    </svg>
    <svg class="back-art-right" role="img" aria-label="Sketch of a farm woman in a headscarf" viewBox="0 0 100 220">
      <rect width="100" height="220" rx="4" fill="#333333"/>
    </svg>

    <p class="story-intro">We are</p>
    <p class="story-name">Lonny and Marva's Vegan Jerky</p>
    <p class="story-body">Our food is vegan, non GMO, straight from the farm, organic, healthy, pure, clean, made in small batches and earth friendly. We use no chemicals or artificial flavors and our product is 100% natural.</p>
    <p class="story-sign">Our kitchen is yours</p>

    <div class="nutrition">
      <h3>NUTRITIONAL INFORMATION*:</h3>
      <p>Serving per package: 2</p>
      <p>Serving Size: 80.05 grams</p>
      <table>
        <tr><th></th><th>Avg. Qty. 80.05g Serve</th><th class="col-split">%*</th><th class="col-split">Avg. Qty. 100g Serve</th></tr>
        <tr><td>ENERGY (kJ)</td><td>305 (kJ)</td><td class="col-split">3.3</td><td class="col-split">814 (kJ)</td></tr>
        <tr><td>Protein</td><td>16 (g)</td><td class="col-split">7</td><td class="col-split">42 (g)</td></tr>
        <tr><td>Vegetable oil</td><td>3 (g)</td><td class="col-split">4</td><td class="col-split">9 (g)</td></tr>
        <tr><td>Carbohydrates</td><td>7 (g)</td><td class="col-split">7</td><td class="col-split">20 (g)</td></tr>
        <tr><td>Sugar</td><td>3 (g)</td><td class="col-split">5</td><td class="col-split">8 (g)</td></tr>
        <tr><td>Sodium</td><td>337 (mg)</td><td class="col-split">14</td><td class="col-split">1125 (mg)</td></tr>
        <tr><td>Saturated fat</td><td>0.2 (g)</td><td class="col-split">1</td><td class="col-split">0.6 (g)</td></tr>
      </table>
    </div>
    <p class="nutrition-note">* Average quantity (Avg. Qty.) based on typical analysis.<br>*% of daily requirements.</p>

    <div class="product-info">
      <p><strong>INGREDIENTS:</strong> Soy protein, Olive Oil, Sugar, Salt, Hydrolyzed vegetable protein, Spices, Vinegar.</p>
      <p><strong>ALLERGENS:</strong> Contains Soy and traces of Gluten.</p>
      <p><strong>STORAGE:</strong> Store at ambient temperature but cool after opening. Consume within 3 days.</p>
      <div class="claims"><span>NON<br>GMO</span><span>100%<br>NATURAL</span></div>
      <p>MANUFACTURED BY<br>Lonny and Marva's Vegan Jerky,<br>Address line, Canada, City</p>
      <p>www.lonnyandmarvasveganjerky.com</p>
    </div>
  </section>

</main>
</body>
</html>
```